175th Anniversary of Family Owned Funeral Home Pole Banners

We are family owned and operated funeral home in the Greater Cincinnati area and operate 3 funeral homes and a cremation center and we will be celebrating our 175th anniversary in 2015. The communities we serve look to us as leaders in the community and we are very well recognized. In preparation for next year, part of our planning includes placing pole banners in our local communities and our funeral home parking areas. The banner dimensions will be 30 x 60. We need for the banners to display a great message of tradition and excellence. Our website is www.brackenholloway.com I have uploaded an example of a pole banner as well as our logo(s).
Updates
Original artwork has been uploaded if needed.
Industry/Entity Type
Funeral Home

```html
<!DOCTYPE html>
<html lang="en">
<head>
<meta charset="utf-8">
<title>Bracken Holloway 175th Anniversary Pole Banner</title>
<link rel="stylesheet" href="https://fonts.googleapis.com/css2?family=Lora:wght@400&family=Poiret+One&display=swap">
<style>
  :root {
    --paper: #fdfcf2;
    --paper-edge: #f3f4e6;
    --brand-blue: #4f7199;
    --sky: #93d8f6;
    --sky-soft: #b9e6f9;
  }
  * { margin: 0; padding: 0; box-sizing: border-box; }
  html, body {
    width: 1200px;
    height: 2400px;
    overflow: hidden;
    background: var(--paper);
  }
  .banner {
    position: relative;
    width: 1200px;
    height: 2400px;
    background: radial-gradient(ellipse at 50% 45%, var(--paper) 55%, var(--paper-edge) 100%);
    overflow: hidden;
  }
  .brand {
    position: absolute;
    top: 40px;
    left: 58px;
    right: 40px;
    display: grid;
    grid-template-columns: 120px 1fr;
    column-gap: 46px;
    align-items: center;
    color: var(--brand-blue);
  }
  .brand-mark {
    width: 120px;
    height: 120px;
    background: var(--brand-blue);
  }
  .brand-name {
    font-family: "Lora", serif;
    font-weight: 400;
    font-size: 112px;
    line-height: 1;
    letter-spacing: 1px;
    white-space: nowrap;
  }
  .brand-tagline {
    grid-column: 1 / 3;
    margin-top: 34px;
    font-family: "Lora", serif;
    font-weight: 400;
    font-size: 55px;
    line-height: 1;
    letter-spacing: 0.5px;
    white-space: nowrap;
  }
  .anniversary-art {
    position: absolute;
    left: 0;
    top: 0;
    width: 1200px;
    height: 2400px;
  }
  .numeral-shape { fill: var(--sky); }
  .numeral-stroke { fill: none; stroke: var(--sky); stroke-width: 40; stroke-linecap: butt; }
  .ordinal, .headline {
    font-family: "Poiret One", sans-serif;
    fill: var(--sky);
  }
  .rule { stroke: var(--sky); stroke-width: 6; }
  .ornament-area { fill: var(--sky-soft); opacity: 0.55; }
</style>
</head>
<body>
  <main class="banner">
    <header class="brand">
      <div class="brand-mark" aria-hidden="true"></div>
      <div class="brand-name">Bracken Holloway</div>
      <div class="brand-tagline">Family Funeral Homes &amp; Cremation Center</div>
    </header>

    <svg class="anniversary-art" viewBox="0 0 1200 2400" xmlns="http://www.w3.org/2000/svg" role="img" aria-label="175th Anniversary">
      <g class="numeral" aria-hidden="true">
        <polygon class="numeral-shape" points="62,705 130,640 172,640 172,1550 130,1550 130,705"/>
        <polygon class="numeral-shape" points="293,640 552,640 292,1670 252,1670 508,682 293,682"/>
        <rect class="numeral-shape" x="660" y="640" width="230" height="40"/>
        <polygon class="numeral-shape" points="660,640 698,640 680,985 640,985"/>
        <path class="numeral-stroke" d="M 662 985 C 740 860 860 850 940 905 C 1080 1000 1110 1300 1060 1480 C 1010 1640 880 1680 780 1640 C 640 1580 560 1380 560 1150"/>
      </g>
      <text class="ordinal" x="942" y="775" font-size="420" textLength="165" lengthAdjust="spacingAndGlyphs">th</text>

      <rect class="ornament-area" x="615" y="1165" width="150" height="235" rx="50" role="img" aria-label="Curling leaf flourish inside the numeral five"/>

      <text class="headline" x="40" y="1960" font-size="330" textLength="1105" lengthAdjust="spacingAndGlyphs">Anniversary</text>

      <line class="rule" x1="40" y1="2045" x2="1148" y2="2045"/>

      <rect class="ornament-area" x="252" y="2085" width="690" height="225" rx="110" role="img" aria-label="Symmetrical scroll flourish beneath the rule"/>
      <rect class="ornament-area" x="0" y="2240" width="160" height="160" rx="40" role="img" aria-label="Leaf flourish in the lower left corner"/>
      <rect class="ornament-area" x="1040" y="2240" width="160" height="160" rx="40" role="img" aria-label="Leaf flourish in the lower right corner"/>
    </svg>
  </main>
</body>
</html>
```